Business Card for New Greek Restaurant

Looking for a Business card for a new Greek Restaurant that's focus is on Take out and Delivery & catering.

Also to outline the contact information for the restaurant.
Does not require a name or title of a specific person (Just general business card)
Phone (519) 372-FETA (3382)
Email : info@bluefigkitchen.ca
Website : www.bluefigkitchen.ca

Facebook/Instagram/Twitter Icons to Follow us as well.

TAKEOUT * DELIVERY* CATERING

Target Market(s)

Woman Age 25-44

Industry/Entity Type

Greek Restaurant

Contact Information for Business Card

Card is to have the general contact information for the business as well as outline our Take Out and Catering Services. Existing Logo attached and to be incorporated into the design.

Font styles to use
Sans Serif

Colors

Designer to choose colors to be used in the design.

Requirements
Must have
• Restaurant Contact Information :
• Phone (519) 372-FETA (3382)
• Email : info@bluefigkitchen.ca
• Website : www.bluefigkitchen.ca
• Highlight Takeout, Catering, Delivery
• Business Address :
• Marlow Crossing
• 27 Hollister Rd., Unit 6
• Breslau ON
• N0B 2K4
Nice to have
• Modern Feel to promote TakeOut and Catering Services.
Should not have
• No Specific Title or Contact Person (Generic Business Card for Restaurant)

```html
<!DOCTYPE html>
<html lang="en">
<head>
<meta charset="utf-8">
<title>Blue Fig Kitchen – Business Card</title>
<link rel="stylesheet" href="https://fonts.googleapis.com/css2?family=Roboto:wght@400;500;700&display=swap">
<style>
  :root {
    --backdrop: #d9d9d9;
    --brand-blue: #1ab9ea;
    --paper: #ffffff;
    --card-shadow: rgba(0, 0, 0, 0.22);
  }
  html, body {
    margin: 0;
    padding: 0;
    overflow: hidden;
  }
  body {
    width: 1200px;
    height: 909px;
    background: var(--backdrop);
    position: relative;
    font-family: "Roboto", Arial, sans-serif;
  }
  .card {
    position: absolute;
    border-radius: 40px;
    overflow: hidden;
    box-shadow: 0 4px 10px var(--card-shadow);
  }
  .card--back {
    left: 64px;
    top: 200px;
    width: 508px;
    height: 509px;
    background: var(--brand-blue);
  }
  .card--front {
    left: 631px;
    top: 202px;
    width: 504px;
    height: 507px;
    background: var(--brand-blue);
  }
  .back__header {
    position: absolute;
    left: 0;
    top: 0;
    width: 100%;
    height: 254px;
    background: var(--paper);
  }
  .brand-name {
    position: absolute;
    left: 0;
    width: 100%;
    text-align: center;
    font-weight: 700;
    text-transform: uppercase;
    line-height: 1;
    margin: 0;
  }
  .brand-name span { display: block; }
  .back__header .brand-name {
    top: 78px;
    color: var(--brand-blue);
    font-size: 50px;
    letter-spacing: 3px;
  }
  .card--front .brand-name {
    top: 196px;
    color: var(--paper);
    font-size: 60px;
    letter-spacing: 4px;
  }
  .brand-name span + span { margin-top: 10px; }

  .follow {
    position: absolute;
    top: 279px;
    left: 0;
    width: 100%;
    display: flex;
    justify-content: center;
    align-items: center;
    gap: 8px;
    color: var(--paper);
    font-size: 19px;
    line-height: 22px;
  }
  .follow__icons { display: flex; gap: 6px; margin-left: 4px; }
  .social-dot {
    width: 21px;
    height: 21px;
    border-radius: 50%;
    background: var(--paper);
  }
  .contact {
    position: absolute;
    top: 322px;
    left: 0;
    width: 100%;
    margin: 0;
    padding: 0;
    list-style: none;
    text-align: center;
    color: var(--paper);
    font-size: 17.5px;
    line-height: 21px;
  }
  .address {
    position: absolute;
    top: 393px;
    left: 0;
    width: 100%;
    margin: 0;
    text-align: center;
    color: var(--paper);
    font-style: normal;
    font-size: 14px;
    line-height: 18px;
  }
  .address span { display: block; }
  .services {
    position: absolute;
    top: 450px;
    left: 0;
    width: 100%;
    height: 22px;
  }
  .services__rule {
    position: absolute;
    top: 10px;
    height: 3px;
    background: var(--paper);
  }
  .services__rule--left { left: 0; width: 92px; }
  .services__rule--right { left: 410px; width: 98px; }
  .services__text {
    position: absolute;
    left: 0;
    width: 100%;
    text-align: center;
    color: var(--paper);
    font-weight: 700;
    font-size: 16px;
    line-height: 22px;
    letter-spacing: 0.2px;
  }
</style>
</head>
<body>
  <section class="card card--back" aria-label="Business card, contact side">
    <div class="back__header">
      <h1 class="brand-name"><span>Blue Fig</span><span>Kitchen</span></h1>
    </div>
    <div class="follow">
      <span>Follow us</span>
      <span class="follow__icons" aria-label="Social profiles">
        <span class="social-dot"></span>
        <span class="social-dot"></span>
        <span class="social-dot"></span>
      </span>
    </div>
    <ul class="contact">
      <li>P : (519) 372-FETA (3382)</li>
      <li>E : info@bluefigkitchen.ca</li>
      <li>W : www.bluefigkitchen.ca</li>
    </ul>
    <address class="address">
      <span>Marlow Crossing, 27 Hollister Rd., Unit 6</span>
      <span>Breslau ON&nbsp; N0B 2K4</span>
    </address>
    <div class="services">
      <span class="services__rule services__rule--left"></span>
      <span class="services__text">TAKEOUT * DELIVERY* CATERING</span>
      <span class="services__rule services__rule--right"></span>
    </div>
  </section>

  <section class="card card--front" aria-label="Business card, brand side">
    <h2 class="brand-name"><span>Blue Fig</span><span>Kitchen</span></h2>
  </section>
</body>
</html>
```